Quorvex clinic business card - double sided for young clinic

I require business cards for my aesthetic clinic specialising in the below treatments. I would like the cards to be modern as my clinic base are young 22-35 years old. I require my logo on it and would like the edges to be rounded.

I have an aesthetic clinic specialising in :
Quorvex
Lip Enhancement
Chemical Peels
Facial Fillers
Non Surgical Face Lift

I would the cards to have the following information on them:
My logo - (in grey/silver)
address
Phone number
services

Colours :
White/grey/silver and red

a nice image on there, perhaps a set of lips as this is a main service i deliver

Company Name: PDA Address: 52 Farrowmere Road, 4 Brackwell High Street, KT9 4WQ Phone: 0208 794 2160 Website: www.penningtondoweaesthetics.co.uk

Target Market(s)

clinics 22-45 years old mainly female

Industry/Entity Type

Business

Contact Information for Business Card

as above

Requirements
Must have
• logo
• Address
• Email
• Phone number
• Services i offer
Nice to have
• images

```html
<!DOCTYPE html>
<html lang="en">
<head>
<meta charset="utf-8">
<title>Pennington Dowe Aesthetics – Business Card</title>
<link rel="stylesheet" href="https://fonts.googleapis.com/css2?family=Old+Standard+TT:wght@400;700&display=swap">
<style>
  :root {
    --page-bg: #2b2624;
    --card-bg: #151515;
    --card-bg-edge: #1d1d1d;
    --silver: #a9a9a9;
    --silver-light: #c8c8c8;
    --white: #f2f2f2;
    --red: #c8141b;
    --faint: #3a3a3a;
    --serif: "Old Standard TT", "Times New Roman", serif;
  }
  * { margin: 0; padding: 0; box-sizing: border-box; }
  html, body {
    width: 1200px;
    height: 780px;
    overflow: hidden;
    background: var(--page-bg);
    font-family: var(--serif);
  }
  .canvas {
    position: relative;
    width: 1200px;
    height: 780px;
    display: flex;
    align-items: center;
    justify-content: center;
    gap: 44px;
  }
  .card {
    position: relative;
    width: 520px;
    height: 336px;
    border-radius: 10px;
    background: radial-gradient(ellipse at 40% 30%, var(--card-bg-edge), var(--card-bg) 70%);
    box-shadow: 0 18px 40px rgba(0,0,0,0.45);
    overflow: hidden;
    color: var(--white);
  }

  /* Front */
  .card-front {
    display: flex;
    flex-direction: column;
    align-items: center;
    padding-top: 30px;
  }
  .brand-mark {
    display: flex;
    align-items: center;
    gap: 12px;
  }
  .brand-mark__dot {
    width: 18px;
    height: 18px;
    border-radius: 50%;
    background: var(--silver);
  }
  .brand-mark__name {
    font-size: 40px;
    font-weight: 400;
    letter-spacing: 4px;
    color: var(--silver-light);
  }
  .brand-name {
    margin-top: 14px;
    text-align: center;
    color: var(--silver);
    line-height: 1;
  }
  .brand-name__primary {
    display: block;
    font-size: 17px;
    letter-spacing: 4px;
  }
  .brand-name__secondary {
    display: block;
    margin-top: 4px;
    font-size: 31px;
    letter-spacing: 6px;
  }
  .divider {
    width: 370px;
    height: 1px;
    margin-top: 12px;
    background: var(--silver);
  }
  .contact {
    margin-top: 22px;
    text-align: center;
    font-weight: 700;
    font-size: 14px;
    line-height: 1.75;
    color: var(--white);
  }
  .front-rule {
    position: absolute;
    left: 75px;
    right: 75px;
    bottom: 28px;
    height: 1px;
    background: var(--silver);
    opacity: 0.8;
  }

  /* Back */
  .card-back .watermark {
    position: absolute;
    left: 50%;
    top: 52%;
    transform: translate(-50%, -50%);
    font-size: 150px;
    letter-spacing: 10px;
    color: var(--faint);
    font-weight: 400;
    white-space: nowrap;
  }
  .services {
    position: relative;
    display: flex;
    flex-direction: column;
    align-items: center;
    padding-top: 64px;
  }
  .services__title {
    font-size: 22px;
    font-weight: 700;
    color: var(--red);
  }
  .services__rule {
    width: 470px;
    height: 2px;
    margin-top: 8px;
    background: var(--red);
  }
  .services__list {
    list-style: none;
    margin-top: 20px;
    text-align: center;
    font-size: 17px;
    font-weight: 700;
    line-height: 1.6;
    color: var(--white);
  }
</style>
</head>
<body>
<main class="canvas">
  <section class="card card-front" aria-label="Business card front">
    <div class="brand-mark">
      <span class="brand-mark__dot"></span>
      <span class="brand-mark__name">PDA</span>
    </div>
    <h1 class="brand-name">
      <span class="brand-name__primary">PENNINGTON DOWE</span>
      <span class="brand-name__secondary">AESTHETICS</span>
    </h1>
    <div class="divider"></div>
    <address class="contact">
      0208 794 2160<br>
      www.penningtondoweaesthetics.co.uk<br>
      52 Farrowmere Road, 4 Brackwell High Street, KT9 4WQ
    </address>
    <div class="front-rule"></div>
  </section>

  <section class="card card-back" aria-label="Business card back">
    <span class="watermark" aria-hidden="true">PDA</span>
    <div class="services">
      <h2 class="services__title">Services</h2>
      <div class="services__rule"></div>
      <ul class="services__list">
        <li>Quorvex</li>
        <li>Lip Enhancement</li>
        <li>Chemical Peels</li>
        <li>Facial Fillers</li>
        <li>Non Surgical Face Lift</li>
      </ul>
    </div>
  </section>
</main>
</body>
</html>
```